Thornwell Building Company - advertisement poster

I am looking to print some canvas signs to advertise my general contracting company, Thornwell Building Company. The sign will measure 6' long x 3' high so the size should match that ratio. I already have a logo icon, which is the Letter 'A' and some trees that I would like to incorporate, see attached. I would also like the to have the following information listed:
1) phone number: 472-318-6095
2) email: thornwellbuildingcompany@mailvistra.net
3) website: thornwellbuildingcompany.com
4) Lic#5386204
5) I want to use this text: "BUILD WITH THE T-CREW!"

The ad should be relatively simple and clean. Black and Green are my company colors. I am open to creative ideas!

Target Market(s)

People looking to renovate their homes

Industry/Entity Type

Construction

Colors
59FF00
82FF00
B8FF75
E3FFCB
F4FFEA

Requirements
Must have
• Must have my company logo
Should not have
• No photos or complex graphics

```html
<!DOCTYPE html>
<html lang="en">
<head>
<meta charset="utf-8">
<title>Thornwell Building Company – Sign</title>
<link rel="stylesheet" href="https://fonts.googleapis.com/css2?family=Arimo:wght@700&family=Nunito+Sans:wght@400;800&display=swap">
<style>
  :root {
    --ink: #000000;
    --brand-green: #6db447;
    --paper: #ffffff;
    --backdrop: #e8eae8;
  }
  * { margin: 0; padding: 0; box-sizing: border-box; }
  html, body {
    width: 1200px;
    height: 800px;
    overflow: hidden;
    background: var(--backdrop);
  }
  .sign {
    position: absolute;
    left: 40px;
    top: 120px;
    width: 1120px;
    height: 560px;
    background: var(--brand-green);
    overflow: hidden;
  }
  .sign__header {
    position: absolute;
    left: 0; top: 0;
    width: 100%;
    height: 234px;
    background: var(--ink);
  }
  .brand-name {
    position: absolute;
    left: 88px;
    top: 112px;
    display: flex;
    align-items: center;
    gap: 14px;
    color: var(--paper);
    font-family: "Arimo", Arial, sans-serif;
    font-weight: 700;
    font-size: 30px;
    line-height: 1.05;
    letter-spacing: 1px;
    text-transform: uppercase;
  }
  .brand-name__mark {
    width: 18px;
    height: 18px;
    background: var(--brand-green);
    flex: none;
  }
  .tagline {
    position: absolute;
    right: 88px;
    top: 160px;
    color: var(--brand-green);
    font-family: "Nunito Sans", Arial, sans-serif;
    font-weight: 800;
    font-size: 28px;
    letter-spacing: 1px;
  }
  .phone {
    position: absolute;
    left: 0;
    width: 100%;
    top: 258px;
    text-align: center;
    color: var(--ink);
    font-family: "Arimo", Arial, sans-serif;
    font-weight: 700;
    font-size: 152px;
    line-height: 1;
    letter-spacing: -2px;
  }
  .contacts {
    position: absolute;
    left: 80px;
    right: 80px;
    top: 442px;
    display: flex;
    justify-content: space-between;
    align-items: center;
    color: var(--ink);
    font-family: "Nunito Sans", Arial, sans-serif;
    font-weight: 400;
    font-size: 24px;
  }
  .contact { display: flex; align-items: center; gap: 8px; }
  .contact__icon { width: 22px; height: 22px; flex: none; }
  .licence {
    position: absolute;
    left: 86px;
    right: 88px;
    top: 512px;
    display: flex;
    align-items: center;
    gap: 12px;
    color: var(--ink);
    font-family: "Arimo", Arial, sans-serif;
    font-weight: 700;
    font-size: 20px;
    letter-spacing: 5px;
  }
  .licence__rule {
    flex: 1;
    height: 2px;
    background: var(--ink);
    margin-top: 8px;
  }
</style>
</head>
<body>
  <main class="sign">
    <header class="sign__header">
      <div class="brand-name">
        <span class="brand-name__mark"></span>
        <span>Thornwell<br>Building Company</span>
      </div>
      <p class="tagline">BUILD WITH THE T-CREW!</p>
    </header>

    <p class="phone">472-318-6095</p>

    <div class="contacts">
      <span class="contact">
        <svg class="contact__icon" viewBox="0 0 24 24" aria-hidden="true">
          <circle cx="12" cy="12" r="11" fill="var(--ink)"/>
          <rect x="6" y="8" width="12" height="8.5" rx="1" fill="none" stroke="var(--brand-green)" stroke-width="1.6"/>
          <path d="M6.5 8.6 L12 13 L17.5 8.6" fill="none" stroke="var(--brand-green)" stroke-width="1.6"/>
        </svg>
        thornwellbuildingcompany@mailvistra.net
      </span>
      <span class="contact">
        <svg class="contact__icon" viewBox="0 0 24 24" aria-hidden="true" fill="none" stroke="var(--ink)" stroke-width="1.8">
          <circle cx="12" cy="12" r="10"/>
          <ellipse cx="12" cy="12" rx="4.5" ry="10"/>
          <path d="M2 12 H22 M4 7 H20 M4 17 H20"/>
        </svg>
        thornwellbuildingcompany.com
      </span>
    </div>

    <div class="licence">
      <span>LIC#5386204</span>
      <span class="licence__rule"></span>
    </div>
  </main>
</body>
</html>
```